Playful, Modern Brochure Design for informing about managed services provided

For our Managed Services we are looking for a brochure with simple explanation of the services we offer. Brochure not a full text brochure. Something like a summation with prices of the options we provide. Think about monitoring, VOIP, anti-virus, quillo 270 etc.

combination of Who We Are and products offering in a simple overview.

a bit similar to https://leaflet.pambervault.com/entry.aspx?id=8830412

it’s about professional services, security and stability of the customers IT, so the design should express that.

Target Market(s)

Business to Business

Font styles to use
Sans Serif
Other font styles liked:
• Arial

Colors

Designer to choose colors to be used in the design.

Requirements
Must have
• attractive front which invites to read further, inside summation of services.
• Contact Info
• Icons for services:
• Hosting, Security, Monitoring, Cloud, VOIP, Online Backup
Nice to have
• Other icons like Quillo 270, firewall, proxy server and other thinkable.
Should not have
• Pages with large amount of text.

```html
<!DOCTYPE html>
<html lang="nl">
<head>
<meta charset="utf-8">
<title>Veltra Computer Services – Managed Services brochure</title>
<link href="https://fonts.googleapis.com/css2?family=Roboto+Condensed:wght@400;700&family=Open+Sans:wght@400;600;700&display=swap" rel="stylesheet">
<style>
:root{
  --blue:#1a8fd8;
  --blue-dark:#0f6fb0;
  --navy:#1b2638;
  --navy-2:#2b3a52;
  --red:#e0343a;
  --grey:#6d6d6d;
  --grey-line:#8a8a8a;
  --text:#5c5c5c;
  --paper:#ffffff;
  --stage:#2b2b2b;
}
*{margin:0;padding:0;box-sizing:border-box}
html,body{width:813px;height:1200px;overflow:hidden;background:var(--stage)}
body{position:relative;font-family:"Open Sans",Arial,sans-serif;color:var(--text)}
.spread{position:absolute;width:508px;height:361px;background:var(--paper);overflow:hidden}
.spread--front{left:152px;top:30px}
.spread--security{left:157px;top:412px}
.spread--cloud{left:157px;top:799px}
.spread svg.shapes{position:absolute;left:0;top:0;width:508px;height:361px}
.abs{position:absolute}
.cond{font-family:"Roboto Condensed",Arial,sans-serif}
.small{font-size:4.6px;line-height:1.55}
.brand{font-family:"Roboto Condensed",Arial,sans-serif;font-weight:700;color:var(--blue);letter-spacing:1px;line-height:1}
.brand small{display:block;font-size:4.3px;letter-spacing:1.6px;color:var(--blue);font-weight:700;margin-top:2px}
.brand .dot{display:inline-block;width:8px;height:8px;border-radius:50%;background:var(--blue);margin-right:4px;vertical-align:1px}

/* front */
.intro-title{left:21px;top:34px;width:230px;font-size:6.4px;font-weight:700;color:var(--blue);line-height:1.45}
.intro-text{left:21px;top:58px;width:226px}
.expect{left:21px;top:109px;font-size:5px}
.bullets{font-size:4.6px;list-style:none}
.bullets li{margin-bottom:7px}
.bullets li::before{content:"";display:inline-block;width:2.5px;height:2.5px;border-radius:50%;background:var(--blue);margin-right:4px;vertical-align:1px}
.map{left:28px;top:226px;width:56px;height:56px;border-radius:50%;background:radial-gradient(circle at 45% 45%,#eef0ec,#d9ddd4);border:2px solid #fff;box-shadow:0 0 0 1px #ccd}
.follow{left:8px;top:331px;color:#fff;font-size:7px}
.follow-dots{left:8px;top:342px;display:flex;gap:3px}
.follow-dots i{width:7px;height:7px;border-radius:50%;background:#fff;display:block}
.question{left:150px;top:200px;width:89px;text-align:right;color:#fff;font-size:5.6px;line-height:1.45}
.contact-title{left:118px;top:241px;color:#fff;font-weight:700;font-size:7.4px;border-bottom:1px solid #fff;padding-bottom:1px}
.contact-list{left:118px;top:254px;list-style:none;color:#fff;font-size:4.8px}
.contact-list li{display:flex;align-items:center;height:14.5px}
.contact-list li span.ic{width:9px;height:9px;border:0.8px solid #fff;border-radius:50%;margin-right:6px;display:flex;align-items:center;justify-content:center}
.legal{left:118px;top:314px;color:#fff;font-size:5.2px;line-height:1.7}
.legal b{font-weight:700}
.svc-label{color:#fff;font-size:5.2px;font-weight:700}
.front-web{left:410px;top:338px;color:#fff;font-size:10px;display:flex;align-items:center;gap:5px}
.front-web i,.foot-web i{width:7px;height:7px;border-radius:50%;border:1.2px solid #fff;display:block}

/* security */
.page-title{left:20px;top:18px;font-family:"Roboto Condensed",Arial,sans-serif;font-weight:700;font-size:27px;color:var(--blue);letter-spacing:.5px}
.title-rule{left:20px;top:51px;width:470px;height:1px;background:#9a9a9a}
.lead{top:65px;width:216px;font-size:5px;line-height:1.5;color:#777}
.svc-head{font-family:"Roboto Condensed",Arial,sans-serif;font-size:9.8px;top:128px}
.svc-head.red{color:var(--red)}
.svc-head.blue{color:var(--blue)}
.svc-body{top:142px;width:99px;font-size:4.3px;line-height:1.6;text-align:justify;color:#808080}
.foot-web{color:#fff;font-size:8px;display:flex;align-items:center;gap:5px}
.newsletter{right:18px;top:327px;text-align:right;color:#fff}
.newsletter .cond{font-size:10.5px}
.newsletter .mail{font-size:7.4px;display:flex;justify-content:flex-end;align-items:center;gap:4px}
.newsletter .mail i{width:6px;height:6px;border-radius:50%;border:1px solid #fff;display:block}

/* cloud */
.cloud-title{left:159px;top:60px;font-family:"Roboto Condensed",Arial,sans-serif;font-weight:700;font-size:29px;color:var(--blue)}
.svc-h{font-family:"Roboto Condensed",Arial,sans-serif;font-size:15px;display:flex;align-items:center;gap:5px}
.svc-h.red{color:var(--red)}
.svc-h.blue{color:var(--blue)}
.svc-p{font-size:4.4px;line-height:1.6;color:#808080}
.helpdesk{right:18px;top:325px;text-align:right;color:#fff}
.helpdesk .cond{font-size:12.5px}
.helpdesk .cond b{font-weight:700}
.helpdesk .hours{font-size:5.6px}
</style>
</head>
<body>

<!-- ================= FRONT / BACK COVER ================= -->
<section class="spread spread--front">
  <svg class="shapes" viewBox="0 0 508 361" role="img" aria-label="Foto van handen die een netwerk van zakelijke pictogrammen van mensen dragen">
    <defs>
      <linearGradient id="navyPhoto" x1="0" y1="0" x2="1" y2="1">
        <stop offset="0" stop-color="#1a2638"/>
        <stop offset=".6" stop-color="#243248"/>
        <stop offset="1" stop-color="#3a4860"/>
      </linearGradient>
    </defs>
    <path d="M66 361 C70 240 170 125 508 80 L508 361 Z" fill="url(#navyPhoto)"/>
    <path d="M175 165 C290 100 400 75 508 58 L508 80 C380 92 270 118 175 165 Z" fill="var(--blue)"/>
    <path d="M66 361 C70 240 170 125 508 80" fill="none" stroke="var(--grey-line)" stroke-width="4"/>
    <path d="M240 361 C350 345 450 295 508 222 L508 361 Z" fill="var(--blue)"/>
    <path d="M240 361 C350 345 450 295 508 222" fill="none" stroke="var(--grey-line)" stroke-width="4"/>
    <path d="M0 288 C40 300 60 330 66 361 L0 361 Z" fill="var(--blue)"/>
    <line x1="254" y1="0" x2="254" y2="4" stroke="#bbb" stroke-width=".5"/>
  </svg>

  <h2 class="abs intro-title">IT PROFESSIONAL MET EEN VERTROUWDE EN PERSOONLIJKE BENADERING</h2>
  <p class="abs intro-text small">Veltra Computer Services in Bergveld zorgt ervoor dat u kunt rekenen op een betrouwbaar bedrijfssysteem. Met een enthousiast team van jonge IT professionals staan wij klaar voor elke IT vraag. Wij staan bekend om onze vertrouwde en persoonlijke benadering, waarbij we technische informatie in begrijpelijke taal aan u communiceren.</p>
  <p class="abs expect">Wat je bij ons kunt verwachten:</p>
  <ul class="abs bullets" style="left:21px;top:124px"><li>Doelgerichte oplossingen</li><li>Duidelijke taal</li></ul>
  <ul class="abs bullets" style="left:106px;top:124px"><li>Eerlijk advies</li><li>Persoonlijk contact</li></ul>

  <div class="abs brand" style="left:293px;top:24px;font-size:21px"><span class="dot"></span>VELTRA<small style="padding-left:12px">COMPUTER SERVICES</small></div>
  <div class="abs brand" style="left:21px;top:178px;font-size:15px"><span class="dot" style="width:6px;height:6px"></span>VELTRA<small style="padding-left:10px;font-size:3.6px">COMPUTER SERVICES</small></div>

  <div class="abs map" role="img" aria-label="Kaartje met de locatie van het kantoor"></div>
  <p class="abs follow">Volg ons op</p>
  <div class="abs follow-dots"><i></i><i></i><i></i><i></i></div>

  <p class="abs question">Heb je een vraag<br>Of kunnen we iets voor u doen?<br>Voel je vrij om contact met<br>ons op te nemen.</p>
  <p class="abs contact-title">Neem contact met ons op</p>
  <ul class="abs contact-list">
    <li><span class="ic"><svg width="5" height="6" viewBox="0 0 10 12"><path d="M5 0a4 4 0 0 1 4 4c0 3-4 8-4 8S1 7 1 4a4 4 0 0 1 4-4z" fill="#fff"/></svg></span>Lindenhoflaan 14 4811 AB Bergveld</li>
    <li><span class="ic"><svg width="5" height="4" viewBox="0 0 10 8"><rect width="10" height="8" fill="#fff"/><path d="M0 0l5 4 5-4" stroke="#1b2638" fill="none"/></svg></span>info@veltra.nl</li>
    <li><span class="ic"><svg width="5" height="5" viewBox="0 0 10 10"><path d="M2 0l2 3-1 1.5c.8 1.5 2 2.7 3.5 3.5L8 7l2 2-1.5 1C4 10 0 6 0 1.5z" fill="#fff"/></svg></span>088-0412300</li>
    <li><span class="ic"><svg width="5" height="5" viewBox="0 0 10 10"><circle cx="5" cy="5" r="4" stroke="#fff" fill="none"/><path d="M1 5h8M5 1v8" stroke="#fff"/></svg></span>www.veltra.nl</li>
  </ul>
  <p class="abs legal"><b>KvK :</b> 40291853<br><b>Bank :</b> NL12BANK0123456789</p>

  <svg class="shapes" viewBox="0 0 508 361" aria-hidden="true">
    <g fill="#fff" stroke="#7a7a7a" stroke-width="2">
      <circle cx="318" cy="317" r="20"/><circle cx="360" cy="299" r="16"/><circle cx="397" cy="279" r="14"/>
      <circle cx="431" cy="258" r="12"/><circle cx="457" cy="239" r="10"/><circle cx="480" cy="220" r="10"/>
    </g>
    <g fill="none" stroke="#555" stroke-width="1.6">
      <path d="M318 305v16M312 315l6 7 6-7M309 326h18"/>
      <path d="M352 292h16v10h-16zM356 306h8"/>
      <path d="M390 284a4 4 0 0 1 2-7 5 5 0 0 1 9-1 3.5 3.5 0 0 1 2 8z"/>
      <path d="M425 253h12v8h-12zM429 264h4"/>
      <path d="M457 233l5 2v4c0 3-2 5-5 6-3-1-5-3-5-6v-4z"/>
      <ellipse cx="480" cy="215" rx="5" ry="2"/><path d="M475 215v9c0 1 2 2 5 2s5-1 5-2v-9M475 220c0 1 2 2 5 2s5-1 5-2"/>
    </g>
  </svg>
  <span class="abs svc-label" style="left:298px;top:342px">Online Backup</span>
  <span class="abs svc-label" style="left:353px;top:319px">VOIP</span>
  <span class="abs svc-label" style="left:389px;top:297px">Cloud</span>
  <span class="abs svc-label" style="left:414px;top:274px">Monitoring</span>
  <span class="abs svc-label" style="left:447px;top:252px">Security</span>
  <span class="abs svc-label" style="left:470px;top:233px">Hosting</span>
  <p class="abs front-web"><i></i>www.veltra.nl</p>
</section>

<!-- ================= SECURITY SPREAD ================= -->
<section class="spread spread--security">
  <svg class="shapes" viewBox="0 0 508 361">
    <defs>
      <linearGradient id="secPhoto" x1="0" y1="0" x2="1" y2="0">
        <stop offset="0" stop-color="#9aa2ab"/><stop offset=".5" stop-color="#d5d9de"/><stop offset="1" stop-color="#ffffff" stop-opacity="0"/>
      </linearGradient>
      <radialGradient id="roomPhoto"><stop offset="0" stop-color="#a8adb3"/><stop offset="1" stop-color="#5f6770"/></radialGradient>
      <radialGradient id="serverPhoto"><stop offset="0" stop-color="#5d7088"/><stop offset="1" stop-color="#1f2a38"/></radialGradient>
    </defs>
    <rect x="4" y="200" width="300" height="160" fill="url(#secPhoto)" role="img" aria-label="Foto van zakenman met een schild en slot als symbool voor beveiliging"/>
    <circle cx="398" cy="266" r="49" fill="url(#roomPhoto)" stroke="#fff" stroke-width="2" role="img" aria-label="Foto van een kantoor met werkplekken"/>
    <circle cx="322" cy="287" r="38" fill="url(#serverPhoto)" stroke="#fff" stroke-width="2" role="img" aria-label="Foto van serverkasten in een datacenter"/>
    <path d="M0 300 C120 360 330 360 508 235 L508 361 L0 361 Z" fill="var(--blue)"/>
    <path d="M0 300 C120 360 330 360 508 235" fill="none" stroke="var(--grey-line)" stroke-width="4"/>
    <line x1="254" y1="0" x2="254" y2="4" stroke="#bbb" stroke-width=".5"/>
  </svg>
  <h1 class="abs page-title">SECURITY</h1>
  <div class="abs title-rule"></div>
  <p class="abs lead" style="left:20px">Wij beschermen uw netwerk, data en werkplekken tegen dreigingen van buitenaf. Met actieve bewaking en vaste updates blijft uw omgeving veilig en stabiel, zodat u zich volledig kunt richten op uw eigen werk en klanten.</p>
  <p class="abs lead" style="left:268px">Onze specialisten richten de beveiliging in op maat van uw bedrijf. Wij controleren dagelijks de status, lossen meldingen direct op en adviseren u over verbeteringen, zodat problemen worden voorkomen voordat ze ontstaan.</p>

  <h3 class="abs svc-head red" style="left:21px">MANAGED FIREWALL</h3>
  <h3 class="abs svc-head blue" style="left:134px">PROXY SERVER</h3>
  <h3 class="abs svc-head red" style="left:269px">ANTI- VIRUS</h3>
  <h3 class="abs svc-head blue" style="left:376px">ONLINE BACKUP SERVICES</h3>
  <p class="abs svc-body" style="left:21px">Een beheerde firewall die al het verkeer naar uw netwerk controleert. Wij houden de regels actueel en blokkeren ongewenste toegang direct, dag en nacht, zonder gedoe voor u.</p>
  <p class="abs svc-body" style="left:134px">De proxy server filtert internetverkeer van uw medewerkers. Zo worden schadelijke websites geweerd en blijft de verbinding snel en betrouwbaar voor het hele kantoor.</p>
  <p class="abs svc-body" style="left:269px">Centraal beheerde virusbescherming op al uw werkplekken en servers. Updates gaan automatisch en bij een melding grijpen wij meteen in.</p>
  <p class="abs svc-body" style="left:376px">Dagelijkse automatische back-up van uw bestanden naar een veilig datacenter. Bij verlies zetten wij uw gegevens snel terug.</p>

  <p class="abs foot-web" style="left:30px;top:341px"><i></i>www.veltra.nl</p>
  <div class="abs newsletter"><p class="cond">Meld je aan voor onze nieuwsbrief</p><p class="mail"><i></i>info@veltra.nl</p></div>
</section>

<!-- ================= CLOUD SPREAD ================= -->
<section class="spread spread--cloud">
  <svg class="shapes" viewBox="0 0 508 361">
    <defs>
      <radialGradient id="cloudPhoto"><stop offset="0" stop-color="#7d8fa3"/><stop offset="1" stop-color="#2e3746"/></radialGradient>
      <linearGradient id="headsetPhoto" x1="0" y1="0" x2="1" y2="1"><stop offset="0" stop-color="#c9b9b0"/><stop offset=".5" stop-color="#e2e2e4"/><stop offset="1" stop-color="#9aa0a8"/></linearGradient>
      <linearGradient id="controlPhoto" x1="0" y1="0" x2="1" y2="0"><stop offset="0" stop-color="#cfd3d8"/><stop offset=".55" stop-color="#3a6fa8"/><stop offset="1" stop-color="#1d3f6b"/></linearGradient>
      <radialGradient id="cityPhoto"><stop offset="0" stop-color="#8aa6c2"/><stop offset="1" stop-color="#1f3148"/></radialGradient>
    </defs>
    <circle cx="78" cy="76" r="59" fill="url(#cloudPhoto)" stroke="var(--blue)" stroke-width="2" role="img" aria-label="Foto van zakenman met handen rond een wolksymbool met slot"/>
    <rect x="254" y="4" width="250" height="116" fill="url(#headsetPhoto)" role="img" aria-label="Foto van een headset op een toetsenbord"/>
    <rect x="4" y="230" width="250" height="100" fill="url(#controlPhoto)" role="img" aria-label="Foto van een medewerker voor een wand met monitoren"/>
    <circle cx="441" cy="249" r="58" fill="url(#cityPhoto)" role="img" aria-label="Foto van een stadsgezicht bij nacht met verbonden netwerklijnen"/>
    <path d="M0 327 C150 345 380 325 508 268 L508 361 L0 361 Z" fill="var(--blue)"/>
    <path d="M0 327 C150 345 380 325 508 268" fill="none" stroke="var(--grey-line)" stroke-width="4"/>
    <line x1="254" y1="0" x2="254" y2="4" stroke="#bbb" stroke-width=".5"/>
  </svg>
  <h1 class="abs cloud-title">CLOUD</h1>

  <h3 class="abs svc-h red" style="left:24px;top:154px"><svg width="11" height="12" viewBox="0 0 11 12"><rect x="1" y="1" width="9" height="10" fill="none" stroke="var(--red)" stroke-width="2"/></svg>QUILLO 270</h3>
  <p class="abs svc-p" style="left:24px;top:175px;width:100px;text-align:justify">Werk overal met uw mail, agenda en documenten. Wij regelen de licenties, migratie en het beheer, zodat uw team direct aan de slag kan.</p>
  <h3 class="abs svc-h blue" style="left:142px;top:154px"><svg width="10" height="11" viewBox="0 0 10 11"><path d="M3 7a3 3 0 1 1 4 0v1H3z M3 10h4" fill="none" stroke="var(--blue)" stroke-width="1.2"/></svg>HOSTING</h3>
  <p class="abs svc-p" style="left:142px;top:175px;width:100px;text-align:justify">Uw website, mail en applicaties veilig gehost in een Nederlands datacenter, met vaste prestaties en dagelijkse controle.</p>

  <h3 class="abs svc-h red" style="left:268px;top:133px"><svg width="11" height="11" viewBox="0 0 11 11"><rect x="1" y="1" width="9" height="5" rx="1" fill="var(--red)"/><rect x="2" y="7" width="7" height="3" fill="var(--red)"/></svg>VOIP</h3>
  <p class="abs svc-p" style="left:268px;top:155px;width:232px">Bellen via internet met vaste lage kosten. Uw nummers blijven behouden en u belt overal vandaan, op kantoor, thuis of onderweg met een app.</p>
  <h3 class="abs svc-h red" style="left:270px;top:212px"><svg width="12" height="10" viewBox="0 0 12 10"><path d="M1 4a7 7 0 0 1 10 0M3 6a4 4 0 0 1 6 0" fill="none" stroke="var(--red)" stroke-width="1.3"/><circle cx="6" cy="8.5" r="1.2" fill="var(--red)"/></svg>WIFI</h3>
  <p class="abs svc-p" style="left:270px;top:235px;width:105px">Snel en stabiel draadloos netwerk door het hele pand, met een apart gastnetwerk voor bezoekers.</p>

  <p class="abs foot-web" style="left:30px;top:341px"><i></i>www.veltra.nl</p>
  <div class="abs helpdesk"><p class="cond">HELPDESK : <b>088-041 23 00</b></p><p class="hours">Bereikbaar op werkdagen van 08:00 tot 17:00</p></div>
</section>

</body>
</html>
```